Business Cards for, Telumo Varisenka - Spending Planner, employed by Clear Path Budget Coach - new business based in Brisbane Australia.

Small Business providing 'Spending Planing' services. Helping people, families, homes, businesses achieve their budgeting goals.

Motto: Making Sense Make Dollars

Final design should communicate financial freedom and strong positive growth.

Target Market(s)

Working Families, Finance, Retail,

Industry/Entity Type

Finance

Contact Information for Business Card

Name, Company Title
Mobile details, Email details

Logo Text

Clear Path Budget Coach - Making Sense Make Dollars

Font styles to use
Serif

Requirements
Must have
• Easy to read
Nice to have
• Modern Looking
Should not have
• Not too confusing to understand

```html
<!DOCTYPE html>
<html lang="en">
<head>
<meta charset="utf-8">
<title>Telumo Varisenka – Business Card</title>
<link rel="stylesheet" href="https://fonts.googleapis.com/css2?family=Roboto+Condensed:ital,wght@0,300;0,400;0,700;1,700&display=swap">
<style>
  :root {
    --backdrop: #2b1c14;
    --card-white: #ffffff;
    --band-gold: #cd9036;
    --icon-orange: #f39a3a;
    --ink: #0d0d0d;
    --swoosh: #0a0a0a;
    --photo-warm: #f3dcc6;
    --photo-coin: #c9954f;
  }
  html, body {
    margin: 0;
    width: 1200px;
    height: 1200px;
    overflow: hidden;
    background: var(--backdrop);
  }
  .card {
    position: absolute;
    left: 60px;
    top: 276px;
    width: 1080px;
    height: 648px;
    background: var(--card-white);
    overflow: hidden;
    font-family: "Roboto Condensed", "Arial Narrow", sans-serif;
  }
  .card__photo {
    position: absolute;
    left: 336px;
    top: 144px;
    width: 634px;
    height: 326px;
    background:
      radial-gradient(ellipse 45% 40% at 78% 38%, var(--photo-warm) 0%, rgba(243,220,198,0) 100%),
      radial-gradient(ellipse 60% 45% at 70% 82%, var(--photo-coin) 0%, rgba(201,149,79,0.35) 55%, rgba(255,255,255,0) 100%);
  }
  .card__curves {
    position: absolute;
    left: 0;
    top: 0;
    width: 1080px;
    height: 648px;
  }
  .card__curves .band { fill: var(--band-gold); }
  .card__curves .swoosh { fill: var(--swoosh); }
  .line {
    position: absolute;
    margin: 0;
    line-height: 1;
    white-space: nowrap;
  }
  .name {
    left: 111px;
    top: 80px;
    font-size: 96px;
    font-weight: 700;
    font-style: italic;
    letter-spacing: 1px;
    color: var(--ink);
    text-transform: uppercase;
  }
  .role {
    left: 111px;
    top: 184px;
    font-size: 51px;
    font-weight: 300;
    color: var(--ink);
    text-transform: uppercase;
  }
  .contact-icon {
    position: absolute;
    left: 110px;
    width: 58px;
    height: 58px;
    border-radius: 4px;
    background: var(--icon-orange);
    display: flex;
    align-items: center;
    justify-content: center;
    color: #fff;
  }
  .contact-icon--phone { top: 271px; }
  .contact-icon--email { top: 348px; font-size: 44px; font-weight: 400; }
  .contact-text {
    left: 179px;
    font-size: 31px;
    font-weight: 400;
    color: var(--ink);
  }
  .contact-text--phone { top: 281px; }
  .contact-text--email { top: 358px; }
  .motto {
    left: 0;
    width: 1080px;
    top: 509px;
    text-align: center;
    font-size: 61px;
    font-weight: 300;
    color: #fff;
    text-transform: uppercase;
  }
  .motto strong { font-weight: 700; }
</style>
</head>
<body>
  <div class="card">
    <div class="card__photo" role="img" aria-label="Photo of a hand placing a coin onto rising stacks of coins"></div>

    <svg class="card__curves" viewBox="0 0 1125 675" preserveAspectRatio="none" aria-hidden="true">
      <path class="band" d="M0,430 C300,520 700,530 1125,398 L1125,675 L0,675 Z"/>
      <path class="swoosh" d="M0,430 C300,520 700,530 1125,398 L1125,356 C820,470 420,525 0,430 Z"/>
    </svg>

    <h1 class="line name">Telumo Varisenka</h1>
    <p class="line role">Spending Planner</p>

    <div class="contact-icon contact-icon--phone">
      <svg width="34" height="34" viewBox="0 0 24 24" aria-hidden="true">
        <path fill="#fff" d="M6.6 10.8c1.4 2.8 3.8 5.1 6.6 6.6l2.2-2.2c.3-.3.7-.4 1-.2 1.1.4 2.3.6 3.6.6.6 0 1 .4 1 1V20c0 .6-.4 1-1 1C10.6 21 3 13.4 3 4c0-.6.4-1 1-1h3.5c.6 0 1 .4 1 1 0 1.3.2 2.5.6 3.6.1.3 0 .7-.2 1L6.6 10.8z"/>
      </svg>
    </div>
    <p class="line contact-text contact-text--phone">+123 456 7890</p>

    <div class="contact-icon contact-icon--email">@</div>
    <p class="line contact-text contact-text--email">hi@clearpath.com</p>

    <p class="line motto">Making Sense <strong>Make Dollars</strong></p>
  </div>
</body>
</html>
```